Harborline Energy - needs a business card

Harborline Energy is a U.S. based diesel sourcing and distribution company that supports American oil & gas fields through providing quality product and consistent services.

Target Market(s)

Oil and Gas

Contact Information for Business Card

The background of the card must be white to ensure the logo pops.

Font styles to use
Serif
Sans Serif

Colors

Designer to choose colors to be used in the design.

Requirements
Must have
• Front of Card: Tag line: Harborline Energy, Powering America's Oil & Gas fields.
• Not sure if you guys do this part but just in case...
• Dale Menschow
• Owner/CEO
• C:555.318.4076
• E:Dmenschow@harborlineenergy.example
• W:Harborlineenergy.example
• Locations: Servicing the Powder River, DJ basin and Bakken formations.
• Back of Card: " Frac fueling is what we do. We understand how important diesel fuel is to your operation, which is why our main service line is Frac fueling. We assure our supply and stand by our service"

```html
<!DOCTYPE html>
<html lang="en">
<head>
<meta charset="utf-8">
<title>Harborline Energy — Business Card</title>
<link rel="stylesheet" href="https://fonts.googleapis.com/css2?family=Libre+Baskerville:ital,wght@0,400;0,700;1,400&display=swap">
<style>
  :root {
    --page: #e9e7e3;
    --card-white: #ffffff;
    --navy: #1f3457;
    --ink: #2a2a2a;
    --ink-soft: #555555;
    --rule: #9aa3b2;
    --accent-red: #c4232f;
    --on-navy: #f2f4f8;
  }
  * { box-sizing: border-box; margin: 0; padding: 0; }
  html, body {
    width: 793px;
    height: 1200px;
    overflow: hidden;
    background: var(--page);
  }
  .canvas {
    position: relative;
    width: 793px;
    height: 1200px;
    font-family: "Libre Baskerville", Georgia, serif;
    color: var(--ink);
  }
  .card {
    position: absolute;
    left: 76px;
    width: 640px;
    height: 366px;
    box-shadow: 0 6px 18px rgba(0,0,0,0.18);
  }
  .card--front {
    top: 170px;
    background: var(--card-white);
    text-align: center;
    padding: 34px 36px 0;
  }
  .card--back {
    top: 650px;
    background: var(--navy);
    padding: 70px 64px;
  }
  .brand {
    display: flex;
    align-items: center;
    justify-content: center;
    gap: 12px;
    margin-bottom: 20px;
  }
  .brand__dot {
    width: 26px;
    height: 26px;
    border-radius: 50%;
    background: var(--accent-red);
  }
  .brand__name {
    font-size: 26px;
    font-weight: 700;
    color: var(--navy);
  }
  .tagline {
    font-size: 13px;
    line-height: 1.55;
    color: var(--ink-soft);
  }
  .person__name {
    margin-top: 8px;
    font-size: 21px;
    color: var(--ink);
  }
  .person__title {
    margin-top: 4px;
    font-size: 12px;
    color: var(--ink-soft);
  }
  .divider {
    width: 150px;
    height: 1px;
    background: var(--rule);
    margin: 14px auto 40px;
  }
  .locations {
    font-size: 12px;
    color: var(--ink-soft);
  }
  .contact {
    position: absolute;
    left: 24px;
    right: 24px;
    bottom: 26px;
    display: flex;
    justify-content: space-between;
    font-size: 10.5px;
    color: var(--ink-soft);
  }
  .quote {
    font-style: italic;
    font-size: 17px;
    line-height: 1.7;
    color: var(--on-navy);
  }
</style>
</head>
<body>
<main class="canvas">
  <section class="card card--front" aria-label="Business card front">
    <div class="brand">
      <span class="brand__dot" aria-hidden="true"></span>
      <span class="brand__name">Harborline Energy</span>
    </div>
    <p class="tagline">Harborline Energy<br>Powering America's Oil &amp; Gas fields.</p>
    <h1 class="person__name">Dale Menschow</h1>
    <p class="person__title">Owner/CEO</p>
    <div class="divider"></div>
    <p class="locations">Servicing the Powder River, DJ basin and Bakken formations.</p>
    <div class="contact">
      <span class="contact__phone">C: 555.318.4076</span>
      <span class="contact__email">E: Dmenschow@harborlineenergy.example</span>
      <span class="contact__web">W: Harborlineenergy.example</span>
    </div>
  </section>

  <section class="card card--back" aria-label="Business card back">
    <p class="quote">&ldquo;Frac fueling is what we do. We understand how important diesel fuel is to your operation, which is why our main service line is Frac fueling. We assure our supply and stand by our service.&rdquo;</p>
  </section>
</main>
</body>
</html>
```